brolvin business card design so that it looks better

need a new business card designed. use our website, brolvix.example for example. I attached an example of a previous card we had and liked. this is for law enforcement and we have attached a previous business card as an example. This site forces me to select color and font, ignore those as I picked stuff just to get this completed.

Target Market(s)

law enforcement, local government

Contact Information for Business Card

see the attached example and our website

Font styles to use
Serif

```html
<!DOCTYPE html>
<html lang="en">
<head>
<meta charset="utf-8">
<title>brolvin business card</title>
<link rel="stylesheet" href="https://fonts.googleapis.com/css2?family=Open+Sans:ital,wght@0,400;0,600;0,700;1,400&display=swap">
<style>
  :root {
    --stage: #2a2c30;
    --navy-deep: #0f2f45;
    --navy: #1b4a66;
    --navy-light: #2a6283;
    --paper: #ffffff;
    --ink-grey: #8a8d91;
    --hatch: #d9dcdf;
    --title-grey: #a3a6aa;
  }
  * { box-sizing: border-box; margin: 0; padding: 0; }
  html, body { width: 1200px; height: 900px; overflow: hidden; }
  body {
    background: var(--stage);
    font-family: "Open Sans", sans-serif;
    position: relative;
  }

  /* ---------- portrait front card ---------- */
  .card-front {
    position: absolute;
    left: 110px; top: 150px;
    width: 340px; height: 600px;
    border-radius: 30px;
    overflow: hidden;
    background: var(--paper);
  }
  .card-front .brand-panel {
    position: absolute; inset: 0 0 auto 0;
    height: 270px;
    background: linear-gradient(160deg, var(--navy) 0%, var(--navy-deep) 100%);
    display: flex; align-items: center; justify-content: center;
  }
  .card-front .divider {
    position: absolute; left: 0; right: 0; top: 270px;
    height: 26px;
    background: linear-gradient(90deg, var(--navy-deep), var(--navy-light) 60%, var(--navy-deep));
  }
  .card-front .divider .hatch-strip {
    position: absolute; left: 0; top: 26px;
    width: 150px; height: 10px;
    background: repeating-linear-gradient(135deg, var(--hatch) 0 1px, var(--paper) 1px 4px);
  }
  .wordmark {
    color: var(--paper);
    font-weight: 600;
    letter-spacing: 4px;
    text-transform: uppercase;
  }
  .card-front .wordmark { font-size: 46px; }

  .contact {
    position: absolute; left: 44px; right: 30px; top: 330px;
  }
  .contact .name {
    color: var(--navy);
    font-weight: 700;
    font-size: 22px;
  }
  .contact .role {
    color: var(--title-grey);
    font-size: 13px;
    margin-top: 2px;
    padding-bottom: 8px;
    border-bottom: 2px solid var(--navy);
    width: 78%;
  }
  .contact-list { list-style: none; margin-top: 22px; }
  .contact-list li {
    display: flex; align-items: flex-start; gap: 12px;
    color: var(--ink-grey);
    font-size: 16px;
    line-height: 1.5;
    margin-bottom: 6px;
  }
  .contact-list .icon {
    flex: none;
    width: 20px; height: 20px; margin-top: 3px;
    border-radius: 4px;
    background: var(--navy);
    display: flex; align-items: center; justify-content: center;
  }

  /* ---------- landscape back card ---------- */
  .card-back {
    position: absolute;
    left: 520px; top: 278px;
    width: 600px; height: 344px;
    border-radius: 30px;
    overflow: hidden;
    background: linear-gradient(170deg, var(--navy) 0%, var(--navy-deep) 100%);
  }
  .card-back .wordmark {
    position: absolute; left: 0; right: 0; top: 84px;
    text-align: center;
    font-size: 62px;
  }
  .card-back .band {
    position: absolute; left: 0; right: 0; top: 214px;
    height: 74px;
    background: linear-gradient(180deg, var(--navy-light) 0%, var(--navy) 45%, var(--navy-deep) 100%);
    border-top: 1px solid rgba(255,255,255,0.15);
  }
  .card-back .hatch-bar {
    position: absolute; left: 150px; top: 10px;
    width: 240px; height: 14px;
    background: repeating-linear-gradient(135deg, var(--hatch) 0 1px, var(--paper) 1px 4px);
  }
  .card-back .web {
    position: absolute; left: 150px; top: 32px;
    color: var(--paper);
    font-size: 22px;
    letter-spacing: 1px;
  }
</style>
</head>
<body>

  <article class="card-front" aria-label="Business card front">
    <div class="brand-panel">
      <span class="wordmark">brolvin</span>
    </div>
    <div class="divider"><span class="hatch-strip"></span></div>

    <section class="contact">
      <h1 class="name">Dana Whitfield</h1>
      <p class="role">Founder/Chief Executive Officer</p>
      <ul class="contact-list">
        <li>
          <span class="icon">
            <svg width="12" height="12" viewBox="0 0 24 24"><path fill="#fff" d="M6.6 10.8a15.5 15.5 0 0 0 6.6 6.6l2.2-2.2c.3-.3.7-.4 1-.2 1.1.4 2.3.6 3.6.6.6 0 1 .4 1 1V20c0 .6-.4 1-1 1A17 17 0 0 1 3 4c0-.6.4-1 1-1h3.5c.6 0 1 .4 1 1 0 1.3.2 2.5.6 3.6.1.3 0 .7-.2 1z"/></svg>
          </span>
          555.010.0187
        </li>
        <li>
          <span class="icon">
            <svg width="12" height="12" viewBox="0 0 24 24"><path fill="#fff" d="M3 5h18v14H3z M4 6.5v.6l8 5.4 8-5.4v-.6z" fill-rule="evenodd"/></svg>
          </span>
          dwhitfield@brolvix.example
        </li>
        <li>
          <span class="icon">
            <svg width="12" height="12" viewBox="0 0 24 24"><path fill="#fff" d="M12 2a7 7 0 0 0-7 7c0 5 7 13 7 13s7-8 7-13a7 7 0 0 0-7-7zm0 9.5a2.5 2.5 0 1 1 0-5 2.5 2.5 0 0 1 0 5z"/></svg>
          </span>
          <span>4180 Harbor Ridge Road<br>Suite 210<br>Lakeview, ST 00412</span>
        </li>
      </ul>
    </section>
  </article>

  <article class="card-back" aria-label="Business card back">
    <span class="wordmark">brolvin</span>
    <div class="band">
      <span class="hatch-bar"></span>
      <span class="web">www.brolvix.example</span>
    </div>
  </article>

</body>
</html>
```